Thank you for shopping with us business card

We would like a thank you card for our rebranded business. We used to be "Brindle Goods" but are now "Marlow Finds. Old thank you card and new logo will be attached for reference. New thank you card does not have to be same design as old thank you card, but please use new logo.
Shopmart URL is now marlowfinds.shopmart.example
Instagram is @Marlow_Finds
Email is marlowfinds@mailbox.example
Thank you!

Contact Information for Business Card

Shopmart site, email, Instagram

```html
<!DOCTYPE html>
<html lang="en">
<head>
<meta charset="utf-8">
<title>Marlow Finds – Thank You Card</title>
<link rel="stylesheet" href="https://fonts.googleapis.com/css2?family=Jost:wght@400;500&family=Montserrat:wght@500;600&display=swap">
<style>
  :root {
    --ink: #0b0b0b;
    --paper: #ffffff;
    --backdrop: #d9d9d9;
    --rule: #1a1a1a;
  }
  * { margin: 0; padding: 0; box-sizing: border-box; }
  html, body { width: 848px; height: 1200px; overflow: hidden; }
  body {
    background: var(--backdrop);
    font-family: "Jost", sans-serif;
    color: var(--ink);
    position: relative;
  }
  .card {
    position: absolute;
    left: 84px;
    width: 680px;
    height: 408px;
    box-shadow: 6px 8px 12px rgba(0,0,0,0.25);
    overflow: hidden;
  }
  .card--front { top: 150px; background: var(--ink); color: var(--paper); }
  .card--back { top: 620px; background: var(--paper); }

  /* front */
  .front-mark {
    position: absolute;
    left: 50%; top: 112px;
    width: 120px; height: 120px;
    transform: translateX(-50%);
    border: 3px solid var(--paper);
  }
  .front-name {
    position: absolute;
    left: 0; right: 0; top: 300px;
    text-align: center;
    font-family: "Montserrat", sans-serif;
    font-weight: 600;
    font-size: 31px;
    letter-spacing: 0.5px;
    text-transform: uppercase;
  }

  /* back */
  .corners { position: absolute; inset: 0; width: 100%; height: 100%; }
  .brand-row {
    position: absolute;
    left: 93px; top: 104px;
    display: flex; align-items: center;
  }
  .brand-mark { width: 52px; height: 52px; background: var(--ink); }
  .brand-divider { width: 1px; height: 64px; background: var(--rule); margin: 0 17px 0 18px; }
  .brand-name {
    font-family: "Montserrat", sans-serif;
    font-weight: 500;
    font-size: 19px;
    line-height: 1.3;
    text-transform: uppercase;
  }
  .thanks {
    position: absolute;
    left: 85px; top: 200px;
    width: 511px; height: 80px;
    display: flex;
  }
  .thanks-title {
    width: 230px;
    background: var(--ink);
    color: var(--paper);
    font-size: 23px;
    line-height: 1.2;
    text-transform: uppercase;
    letter-spacing: 0.3px;
    display: flex; flex-direction: column; justify-content: center;
    padding-left: 18px;
    clip-path: polygon(8px 0, 100% 0, 100% 100%, 8px 100%, 0 calc(100% - 8px), 0 8px);
  }
  .thanks-note {
    flex: 1;
    border: 1px solid var(--rule);
    border-left: none;
    border-radius: 0 8px 8px 0;
    font-size: 14px;
    line-height: 1.35;
    padding: 7px 0 0 16px;
  }
  .contacts {
    position: absolute;
    left: 85px; top: 332px;
    display: flex; align-items: center; gap: 7px;
    font-size: 11.5px;
    white-space: nowrap;
  }
  .contact { display: flex; align-items: center; gap: 4px; }
  .icon { width: 17px; height: 17px; flex: none; }
  .icon--circle { border-radius: 50%; background: var(--ink); }
  .icon--square { background: var(--ink); border-radius: 2px; }
</style>
</head>
<body>

<section class="card card--front">
  <div class="front-mark"></div>
  <h1 class="front-name">Marlow Finds</h1>
</section>

<section class="card card--back">
  <svg class="corners" viewBox="0 0 680 408" aria-hidden="true">
    <polygon points="0,0 58,0 0,50" fill="#0b0b0b"/>
    <line x1="58" y1="0" x2="0" y2="50" stroke="#fff" stroke-width="0"/>
    <line x1="0" y1="46" x2="54" y2="0" stroke="#fff" stroke-width="1.5"/>
    <polygon points="680,0 622,0 680,50" fill="#0b0b0b"/>
    <line x1="680" y1="46" x2="626" y2="0" stroke="#fff" stroke-width="1.5"/>
    <polygon points="0,408 62,408 0,356" fill="#0b0b0b"/>
    <line x1="0" y1="362" x2="56" y2="408" stroke="#fff" stroke-width="1.5"/>
    <polygon points="680,408 618,408 680,356" fill="#0b0b0b"/>
    <line x1="680" y1="362" x2="624" y2="408" stroke="#fff" stroke-width="1.5"/>
  </svg>

  <div class="brand-row">
    <div class="brand-mark"></div>
    <div class="brand-divider"></div>
    <div class="brand-name">Marlow<br>Finds</div>
  </div>

  <div class="thanks">
    <div class="thanks-title"><span>Thank you for</span><span>your purchase</span></div>
    <p class="thanks-note">Your purchase made my day and<br>I hope this package brightens yours.<br>Please come back and leave a review!</p>
  </div>

  <div class="contacts">
    <span class="contact"><span class="icon icon--circle"></span>@Marlow_Finds</span>
    <span class="contact"><span class="icon icon--square"></span>marlowfinds@mailbox.example</span>
    <span class="contact">
      <svg class="icon" viewBox="0 0 20 20" aria-hidden="true">
        <circle cx="10" cy="10" r="9" fill="#0b0b0b"/>
        <ellipse cx="10" cy="10" rx="3.8" ry="8.5" fill="none" stroke="#fff" stroke-width="1.2"/>
        <line x1="1.5" y1="10" x2="18.5" y2="10" stroke="#fff" stroke-width="1.2"/>
        <line x1="3" y1="5.5" x2="17" y2="5.5" stroke="#fff" stroke-width="1.2"/>
        <line x1="3" y1="14.5" x2="17" y2="14.5" stroke="#fff" stroke-width="1.2"/>
      </svg>marlowfinds.shopmart.example</span>
  </div>
</section>

</body>
</html>
```